Business Card Design Project

Velvet Harbor is a Boutique Clothing. On the business cards I would like to have this included
Website: www.velvetharbor-example.com
Email: shop@velvetharbor-example.com
Owner: Mai Torres & Bo Rinaldi

Industry/Entity Type

Business

Contact Information for Business Card

I wanted something simple and elegant. I have attach business logo.

```html
<!DOCTYPE html>
<html lang="en">
<head>
<meta charset="UTF-8">
<title>Velvet Harbor — Business Card</title>
<link rel="stylesheet" href="https://fonts.googleapis.com/css2?family=Lato:wght@400;700&display=swap">
<style>
  :root {
    --stage: #2b2b2b;
    --card-light: #f4f4f4;
    --card-dark: #1f1f1f;
    --ink: #222222;
    --ink-soft: #555555;
    --ink-light: #e6e6e6;
    --divider: #cfcfcf;
  }
  * { margin: 0; padding: 0; box-sizing: border-box; }
  html, body {
    width: 1200px; height: 900px; overflow: hidden;
    background: var(--stage);
    font-family: "Lato", Arial, sans-serif;
  }
  .stage {
    position: relative; width: 1200px; height: 900px;
    display: flex; align-items: center; justify-content: center; gap: 40px;
  }
  .card {
    width: 500px; height: 286px; border-radius: 22px;
    position: relative; overflow: hidden;
  }
  .card--front { background: var(--card-light); color: var(--ink); display: flex; }
  .card--back { background: var(--card-dark); color: var(--ink-light);
    display: flex; flex-direction: column; align-items: center; justify-content: center; gap: 34px; }

  .brand-mark {
    display: flex; flex-direction: column; align-items: center; gap: 12px;
  }
  .brand-mark__circle {
    width: 14px; height: 14px; border-radius: 50%;
    border: 2px solid currentColor;
  }
  .brand-mark__name {
    font-weight: 700; font-size: 20px; letter-spacing: 5px;
    text-transform: uppercase; text-align: center; line-height: 1.35;
  }

  .card__brand-panel {
    width: 230px; display: flex; align-items: center; justify-content: center;
  }
  .card__divider {
    width: 1px; background: var(--divider); margin: 40px 0;
  }
  .card__details {
    flex: 1; padding: 62px 0 0 30px;
  }
  .owners { font-weight: 700; font-size: 15px; letter-spacing: 0.2px; text-transform: uppercase; }
  .role { font-size: 11px; color: var(--ink-soft); text-transform: uppercase; margin-top: 3px; letter-spacing: 0.5px; }
  .contact-list { list-style: none; margin-top: 16px; }
  .contact-list li {
    display: flex; align-items: center; gap: 7px;
    font-size: 13px; color: var(--ink); line-height: 19px;
  }
  .contact-list svg { width: 11px; height: 11px; fill: var(--ink); flex: none; }

  .tagline {
    font-size: 15px; letter-spacing: 0.4px; text-transform: uppercase;
  }
</style>
</head>
<body>
<main class="stage">
  <section class="card card--front">
    <div class="card__brand-panel">
      <div class="brand-mark">
        <span class="brand-mark__circle"></span>
        <span class="brand-mark__name">Velvet<br>Harbor</span>
      </div>
    </div>
    <div class="card__divider"></div>
    <div class="card__details">
      <p class="owners">Mai Torres &amp; Bo Rinaldi</p>
      <p class="role">Owner</p>
      <ul class="contact-list">
        <li>
          <svg viewBox="0 0 12 12" aria-hidden="true"><path d="M2.5 1l2 2.3-1 1.3c.7 1.5 1.8 2.6 3.3 3.3l1.3-1L11 8.6 9.8 11C5 10.6 1.4 7 1 2.2z"/></svg>
          555 014 2288
        </li>
        <li>
          <svg viewBox="0 0 12 12" aria-hidden="true"><rect x="0.5" y="2" width="11" height="8" rx="1"/><path d="M1 2.5l5 4 5-4" fill="none" stroke="#f4f4f4" stroke-width="1"/></svg>
          shop@velvetharbor-example.com
        </li>
        <li>
          <svg viewBox="0 0 12 12" aria-hidden="true"><circle cx="6" cy="6" r="5.5"/><path d="M0.5 6h11M6 .5c-2.5 3-2.5 8 0 11M6 .5c2.5 3 2.5 8 0 11" fill="none" stroke="#f4f4f4" stroke-width="0.8"/></svg>
          www.velvetharbor-example.com
        </li>
      </ul>
    </div>
  </section>

  <section class="card card--back">
    <div class="brand-mark">
      <span class="brand-mark__circle"></span>
      <span class="brand-mark__name">Velvet<br>Harbor</span>
    </div>
    <p class="tagline">Save on top brands at Velvet Harbor!</p>
  </section>
</main>
</body>
</html>
```